Mediakit / brochure for Dutch Travel Blog

About our company:
• Bolderwijk.nl is a Travel- & influence network for independent travellers, outdoor geeks, culture lovers & adventure seekers.
• We don’t sell trips by ourself, we inspire other to travel.
• It’s all about travel inspiration.

About the media kit / brochure:
• The media kit itself must be a travel experience / inspiration.
• Colourful and clean design.
• Use the colours of our new logo
• Use our icons (marker, worldmap) in the design
• Use the style of our website.
• All the text in the media kit must be adjustable by us
• Page format: A4
• Number of pages: 6
• It must be printable as a brochure (for presentations)
• We also need a .pdf version of the brochure (for emailing it to our partners)
• Logo kit added: (1a) + (1b) + (1c) Logo sourcefile

Content of the media kit / brochure
• 6 pages
o (1) Front page
o (2) About Us
o (3) Stats / Companies work with
o (4) Advertising
o (5) Back page
o (6) Our contributors

• Example is attached: (2) example of a brochure with 5 pages A4 (don’t like the design of this example for our media kit, but just to show the idea of the 5 pages).

Maybe use a big travel photo that covers all pages?

For detailed information, I attached the document 'Design brochure Bolderwijk (version 2)'.
Updates

Hello designers,Small update for the Cover Page:- Please use one of the images from the attachment I added in the Brief Design: "URL of images for cover.txt"- Use this text "Travel- & influence network for independent travelers, outdoor geeks, culture lovers & adventure seekers."- Add the text MEDIA KIT (remove "2017: )Thanks.Hendrik Added Thursday, January 5, 2017

Target Market(s)

The mediakit / brochure is for our partners (travel organisations, airline companies, PR companies and big brands like Pale Timber Co and Vesko).

And the readers of our website are independent travellers, outdoor geeks and adventure seekers. So the theme of the Mediakit must be 'travel inspiration'.

Industry/Entity Type

Travel Industry

Requirements
Must have
• • The media kit itself must be a travel experience / inspiration.
• • Colourful and clean design.
• • Use the colours of our new logo
• • Use our icons (marker, worldmap) in the design
• • Use the style of our website.
• • All the text in the media kit must be adjustable by us
• • Page format: A4
• • Number of pages: 6
• • It must be printable as a brochure (for presentations)
• • We also need a .pdf version of the brochure (for emailing it to our partners)

```html
<!DOCTYPE html>
<html lang="en">
<head>
<meta charset="utf-8">
<title>Bolderwijk Media Kit – Spread</title>
<link href="https://fonts.googleapis.com/css2?family=Montserrat:wght@400;500;600;700&family=Open+Sans:wght@400;600;700&display=swap" rel="stylesheet">
<style>
:root{
  --pink:#e8317a;--green:#c3d931;--orange:#f6b020;--cyan:#3dc7e6;
  --dark:#363a45;--ink:#2a2c33;--grey:#8c8f96;--light:#bfc2c7;
  --paper:#f7f7f7;--bg:#ece9e4;
}
*{margin:0;padding:0;box-sizing:border-box}
html,body{width:1200px;height:1200px;overflow:hidden;background:var(--bg)}
body{position:relative;font-family:"Open Sans",sans-serif;color:var(--ink)}
.spread{position:absolute;left:45px;top:338px;width:1310px;height:617px;transform:scale(.8473);transform-origin:0 0;background:var(--paper);box-shadow:0 6px 18px rgba(0,0,0,.18)}
.panel{position:absolute;top:0;height:617px;width:437px}
.panel+.panel{border-left:1px solid #e2e2e2}
.p1{left:0}.p2{left:437px;width:436px}.p3{left:873px}
.bar-head{position:absolute;top:25px;left:0;right:0;height:25px;background:var(--dark);color:#fff;font:700 14px "Montserrat",sans-serif;text-align:center;line-height:25px}
.abs{position:absolute}
.label{font:600 12px "Montserrat",sans-serif;color:var(--ink)}
.figure{position:absolute}
.pct{font:600 11px "Montserrat",sans-serif}
.age-row{position:absolute;left:25px;height:14px;display:flex;align-items:center}
.age-row .fill{height:14px;color:#fff;font:400 10px "Open Sans",sans-serif;padding-left:4px;line-height:14px}
.age-row .pct{margin-left:6px}
.map{position:absolute;left:25px;top:315px;width:390px;height:210px;background:linear-gradient(135deg,#8a8c90,#3f4146);border-radius:40px 60px 30px 50px}
.tag{position:absolute;font:600 10px "Montserrat",sans-serif;text-align:center}
.tag b{display:block;color:#fff;padding:1px 3px}
.social{position:absolute;display:flex;gap:6px;width:90px}
.social .sq{width:20px;height:20px;flex:none;margin-top:2px}
.social strong{font:700 13px "Montserrat",sans-serif;display:block;line-height:16px}
.social small{display:block;font-size:8.5px;line-height:11px;color:var(--grey)}
.big{position:absolute;font:700 13px "Montserrat",sans-serif}
.big small{display:block;font:400 10px "Open Sans",sans-serif;line-height:10px}
.p2 h2{position:absolute;left:23px;top:70px;font:500 19px "Montserrat",sans-serif}
.intro{position:absolute;left:23px;top:98px;width:400px;font-size:8.5px;line-height:17.8px}
.partners{position:absolute;left:24px;width:388px;border:1px solid var(--dark);background:#fff}
.partners .band{display:flex;height:78px;background:var(--dark)}
.partners .band h3{width:112px;background:var(--pink);color:#fff;font:700 13px "Montserrat",sans-serif;padding:24px 12px;line-height:15px}
.partners .band p{flex:1;color:#fff;font-size:8.2px;line-height:10px;padding:14px 14px 0}
.logos{display:flex;flex-wrap:wrap;align-items:center;gap:10px 18px;padding:16px 18px}
.logo{display:flex;align-items:center;gap:4px;font:700 11px "Open Sans",sans-serif;white-space:nowrap}
.logo i{width:9px;height:9px;display:inline-block}
.col{position:absolute;top:25px;width:182px;font-size:8.2px;line-height:9.7px;color:var(--grey)}
.col.left{left:25px}.col.right{left:242px;color:var(--ink)}
.pinktxt{color:var(--pink)}
.col h4{color:var(--green);font:600 9px "Montserrat",sans-serif;margin:10px 0 12px;letter-spacing:.3px}
.col ul{list-style:none}
.col li{position:relative;padding-left:13px}
.col li::before{content:"•";position:absolute;left:0}
.col li b{color:var(--ink);font-weight:600;display:block}
.col.right li b{font-weight:700}
.prices{position:absolute;left:25px;top:396px;width:387px;border-collapse:collapse;font-size:8.5px}
.prices th{background:var(--dark);color:#fff;font:700 8.5px "Open Sans",sans-serif;height:15px}
.prices td{background:#c9cbce;color:#eef0f2;height:15.2px;padding:0 14px;border-bottom:1px solid #f4f4f4}
.prices td+td{border-left:1px solid #f4f4f4}
</style>
</head>
<body>
<div class="spread">

  <section class="panel p1">
    <div class="bar-head">AUDIENCE OVERVIEW</div>
    <div class="abs label" style="left:25px;top:74px">GENDER</div>
    <svg class="figure" style="left:103px;top:75px" width="20" height="48" viewBox="0 0 20 48" aria-hidden="true"><circle cx="10" cy="5" r="5" fill="var(--green)"/><path d="M5 12h10l5 18h-5l-1 18h-8l-1-18H0z" fill="#e6d51d"/></svg>
    <div class="abs pct" style="left:134px;top:85px;color:var(--green)">66%</div>
    <div class="abs pct" style="left:134px;top:100px;color:var(--grey)">34%</div>
    <svg class="figure" style="left:170px;top:75px" width="20" height="48" viewBox="0 0 20 48" aria-hidden="true"><circle cx="10" cy="5" r="5" fill="var(--grey)"/><path d="M2 12h16v20h-3v16h-4V32h-2v16H5V32H2z" fill="var(--grey)"/></svg>

    <div class="abs label" style="left:25px;top:144px">AGE</div>
    <div class="age-row" style="top:162px"><span class="fill" style="width:55px;background:var(--pink)">18-24</span><span class="pct" style="color:var(--pink)">11%</span></div>
    <div class="age-row" style="top:182px"><span class="fill" style="width:128px;background:var(--green)">25-34</span><span class="pct" style="color:var(--green)">30%</span></div>
    <div class="age-row" style="top:202px"><span class="fill" style="width:142px;background:var(--orange)">35-44</span><span class="pct" style="color:var(--orange)">36%</span></div>
    <div class="age-row" style="top:222px"><span class="fill" style="width:58px;background:var(--cyan)">45-54</span><span class="pct" style="color:var(--cyan)">12%</span></div>
    <div class="age-row" style="top:242px"><span class="fill" style="width:47px;background:var(--ink)">55-64</span><span class="pct" style="color:var(--ink)">9%</span></div>
    <div class="age-row" style="top:262px"><span class="fill" style="width:25px;background:#9a9ca0">65+</span><span class="pct" style="color:var(--grey)">2%</span></div>

    <div class="abs label" style="left:25px;top:296px">COUNTRIES VISITED</div>
    <div class="map" role="img" aria-label="World map in grey tones showing where readers travel"></div>
    <div class="tag" style="left:88px;top:356px;color:var(--pink)"><b style="background:var(--pink)">19%</b>USA</div>
    <div class="tag" style="left:255px;top:356px;color:var(--green)"><b style="background:var(--green)">81%</b>EUROPE</div>

    <div class="abs label" style="left:224px;top:74px;font-weight:400">TRAFFIC &amp; SOCIAL MEDIA</div>
    <div class="social" style="left:224px;top:97px"><span class="sq" style="background:#3b5a98" aria-label="Friendwall"></span><div><strong>30.000+</strong><small>@bolderwijk</small></div></div>
    <div class="social" style="left:318px;top:97px"><span class="sq" style="background:var(--pink);border-radius:5px" aria-label="Pixfeed"></span><div><strong>5200+</strong><small>@bolderwijk</small></div></div>
    <div class="social" style="left:224px;top:139px"><span class="sq" style="background:#2aa3de" aria-label="Chirpline"></span><div><strong>7000+</strong><small>@bolderwijk</small></div></div>
    <div class="big" style="left:224px;top:182px;color:var(--pink)">115.000+<small>unique visitors<br>month</small></div>
    <div class="big" style="left:224px;top:228px;color:var(--green)">240.000+<small>page views<br>per month</small></div>
  </section>

  <section class="panel p2">
    <div class="bar-head">WE WORK WITH</div>
    <h2>“Let's work together!”</h2>
    <div class="intro">
      <p>Wondering how to transform your product from a commodity into an experience?</p>
      <p>Not sure how to leverage the power of social media and connect with your target demographic?</p>
      <p>Need help aligning your branding with your company values?</p>
      <p>Whether you are a tourism board, travel company, property, or product, we can help.</p>
      <p>We work with more than 100 travel and brand partners.</p>
    </div>
    <div class="partners" style="top:194px">
      <div class="band"><h3>TRAVEL PARTNERS</h3><p>We have worked with some of the world's top travel companies &amp; destinations to help them achieve their goals. They leverage our authority and expertise in social media promotion, cross-marketing campaigns and unique content creation to showcase their offerings.</p></div>
      <div class="logos">
        <span class="logo" style="color:var(--cyan)">Isla Brisa</span>
        <span class="logo" style="color:#1f3f8f">Trailmere</span>
        <span class="logo" style="color:#1a8fd0">Nordwing</span>
        <span class="logo" style="color:#1f3f8f"><i style="background:var(--orange)"></i>Lionsky Air</span>
        <span class="logo" style="color:#1a8fd0">Farescout</span>
        <span class="logo" style="color:#c0392b">Tuktrail</span>
        <span class="logo" style="color:#e2231a"><i style="background:#e2231a;border-radius:50%"></i>Solvia</span>
      </div>
    </div>
    <div class="partners" style="top:388px">
      <div class="band"><h3>BRAND PARTNERS</h3><p>Bolderwijk reaches a niche audience of travellers passionate about unique experiences and amazing products. We have helped countless brands, from fashion labels to major technology corporations, bring their products to The Netherlands and reach their target consumers.</p></div>
      <div class="logos" style="padding:14px 14px;gap:16px;flex-wrap:nowrap">
        <span class="logo" style="color:var(--ink)">Actiq</span>
        <span class="logo" style="color:var(--ink)"><i style="background:#f5d400"></i>Vesko</span>
        <span class="logo" style="color:#a0413a">Ridgepack</span>
        <span class="logo" style="color:#d81f26"><i style="background:#d81f26"></i>Pale Timber Co</span>
        <span class="logo" style="color:var(--ink)">Wayfinder</span>
      </div>
    </div>
  </section>

  <section class="panel p3">
    <div class="col left">
      <p class="pinktxt">Bolderwijk has a large online interactive community through its readers and social networks that provides a perfect venue to showcase your brand or destination to a highly engaged online audience of travel enthusiasts.</p>
      <p class="pinktxt" style="margin-top:10px">Check out some of the things we can do for you.</p>
      <h4>SPONSORSHIP OPPORTUNITIES</h4>
      <ul>
        <li><b>Travel Writing</b>Yes please! Digital Storytelling our core business. About independent &amp; off the beaten path travel. About exciting cities, with their buzzing street life, wild nightlife and unbeatable attractions. About otherworldly landscapes and awe-inspiring natural wonders. Near and afar.</li>
        <li><b>Press &amp; Fam Trips</b>The only thing we love more than experiencing new places is sharing the destinations with our readers. Our travel journalists are invited by tourist offices, airline companies, hotel brands and other partners. In 2016 for example our journalists went to Peru, Norway, South Africa, Costa Rica, Thailand and Spitsbergen.</li>
        <li><b>Reviews / Sponsorship</b>We love reviews! They give us a chance to let our readers know about unique products for the experiential traveler. We'd love to write an honest review for</li>
      </ul>
    </div>
    <div class="col right">
      <p>your app, product, hotel or anything else you can think of!</p>
      <ul>
        <li><b>Traveldirectory</b>Are you the owner of a small romantic B&amp;B in Italy? Or of that cool rafting company in Bali? Or do you have an excellent restaurant on Aruba? We invented our unique traveldirectory for local companies, where we match accommodations, attractions, tours, travelcompanies and restaurants to a specific destination.</li>
        <li><b>Advertising</b>Advertorials, SEO articles, sidebars, banners, social media promotion. We have a lot of interesting advertising opportunities to help your business market its products and services to a target audience and help you expand your brand awareness.</li>
        <li><b>Photography.</b>It's no secret that stunning images are one of the best and easiest ways to showcase your brand or destination. We offer a selection of photography services that help enhance your brands website and social networks.</li>
        <li><b>Travelvlogs</b>Professionally produced and edited Vidcast videos. Showcase your destination through the eyes of a world traveler!</li>
        <li><b>Videography using drones</b>Our state of the art drone footages will blow your mind.</li>
      </ul>
    </div>
    <table class="prices">
      <tr><th colspan="3">ADVERTISING PRICES</th></tr>
      <tr><td>Travel directory</td><td>€ &nbsp;100</td><td style="text-align:right">per year</td></tr>
      <tr><td>Text link</td><td>€ &nbsp;250</td><td style="text-align:right">per year</td></tr>
      <tr><td>Advertorials (max 3 links)</td><td>€ &nbsp;500</td><td></td></tr>
      <tr><td>Sidebars</td><td colspan="2">Please ask for current pricing</td></tr>
      <tr><td>Banners</td><td colspan="2">Please ask for current pricing</td></tr>
      <tr><td>Social shares</td><td></td><td></td></tr>
      <tr><td>· Friendwall</td><td>€ &nbsp;150</td><td></td></tr>
      <tr><td>· Pixfeed</td><td>€ &nbsp;100</td><td></td></tr>
      <tr><td>· Chirpline</td><td>€ &nbsp;&nbsp;50</td><td></td></tr>
      <tr><td>Reviews</td><td>€ &nbsp;250</td><td></td></tr>
      <tr><td>Vidcast video</td><td>€ &nbsp;250</td><td></td></tr>
      <tr><td>Videography using drones</td><td>€ 1.000</td><td></td></tr>
    </table>
  </section>

</div>
</body>
</html>
```